Accounting practice seeks business card redesign with existing logo

Accounting practice has logo and slogan but more needs modern professional business revision. Must be in a file format ready to print quality business cards.

Open to artistic ideas but for the brand recognition the features below must be incorporated:

- Logo: attached in EPS format (Logo now blue)
- Slogan: Proven Business Solutions... That Work! (in orange legible handwriting type font)
- Name: Daniel T Hoxley RBA AAT JP (letters in smaller font)
- Phone icon: 1800 531 908
- Mobile phone icon: 0412 385 714
- Web icon: www.kelnovagroup.com.au
- Email icon: admin@kelnovagroup.com.au
- See pics for dark blue/med blue line at bottom, this is a necessity.
- Globe that forms the 'dot' in the 'I' of KelNova is attached. It is too big at present.
- Rear side: pic attached. Note my logo is a watermark. I Will provide slightly revised wording details later. Please allow for a small white space at bottom of rear of card to write notes/appointment details.

I am open to ideas but must retain the above for brand recognition.

```html
<!DOCTYPE html>
<html lang="en">
<head>
<meta charset="utf-8">
<title>KelNova Business Card</title>
<link rel="stylesheet" href="https://fonts.googleapis.com/css2?family=PT+Sans:wght@400;700&family=Kalam:wght@400&display=swap">
<style>
  :root {
    --navy: #0c1f54;
    --mid-blue: #2a8fd0;
    --orange: #ee7a24;
    --ink: #1d1d1f;
    --paper: #ffffff;
    --backdrop: #e4e6ea;
    --bullet-light: #3a9ad8;
  }
  * { margin: 0; padding: 0; box-sizing: border-box; }
  html, body { width: 1200px; height: 1000px; overflow: hidden; }
  body {
    background: var(--backdrop);
    font-family: "PT Sans", Arial, sans-serif;
    color: var(--ink);
    position: relative;
  }
  .card {
    position: absolute;
    left: 200px;
    width: 800px;
    height: 458px;
    background: var(--paper);
    overflow: hidden;
    box-shadow: 0 6px 18px rgba(0,0,0,0.18);
  }
  .card--front { top: 28px; }
  .card--back { top: 514px; }

  .logo-box {
    position: absolute;
    left: 34px; top: 30px;
    width: 300px; height: 150px;
    background: var(--navy);
    display: flex; align-items: center; justify-content: center;
  }
  .logo-name {
    font-family: "PT Sans", Arial, sans-serif;
    font-weight: 400;
    font-size: 58px;
    letter-spacing: 3px;
    color: #ffffff;
  }
  .slogan {
    position: absolute;
    left: 38px; top: 188px;
    font-family: "Kalam", cursive;
    font-size: 30px;
    color: var(--orange);
  }
  .holder {
    position: absolute;
    left: 518px; top: 222px;
  }
  .holder-name { font-size: 25px; line-height: 1.1; }
  .holder-creds { font-size: 14px; margin-top: 4px; letter-spacing: 0.5px; }
  .contact-list { list-style: none; margin-top: 22px; }
  .contact-list li {
    display: flex; align-items: center;
    font-size: 17px; line-height: 22px;
  }
  .contact-list svg { width: 13px; height: 13px; margin-right: 10px; fill: var(--navy); flex: none; }

  .band { position: absolute; left: 0; bottom: 0; width: 800px; height: 90px; }

  .services {
    position: absolute;
    left: 60px; top: 70px;
    list-style: none;
  }
  .services li {
    font-size: 23px; line-height: 33px;
    display: flex; align-items: center;
  }
  .services li::before {
    content: ""; width: 6px; height: 6px; border-radius: 50%;
    margin-right: 16px; background: var(--navy);
  }
  .services li:nth-child(odd)::before { background: var(--bullet-light); }
</style>
</head>
<body>
  <section class="card card--front" aria-label="Business card front">
    <div class="logo-box"><span class="logo-name">KelNova</span></div>
    <p class="slogan">Proven Business Solutions</p>
    <div class="holder">
      <p class="holder-name">Daniel T Hoxley</p>
      <p class="holder-creds">RBA AAT JP</p>
      <ul class="contact-list">
        <li><svg viewBox="0 0 16 16"><path d="M3 1l3 3-1.6 2.2a9 9 0 0 0 5.4 5.4L12 10l3 3-2 2C6 15 1 10 1 3z"/></svg>1800 531 908</li>
        <li><svg viewBox="0 0 16 16"><path d="M4 0h8a1 1 0 0 1 1 1v14a1 1 0 0 1-1 1H4a1 1 0 0 1-1-1V1a1 1 0 0 1 1-1zm1 2v10h6V2zm3 11a1 1 0 1 0 0 2 1 1 0 0 0 0-2z"/></svg>0412 385 714</li>
        <li><svg viewBox="0 0 16 16"><path d="M0 3h16v10H0zm1.5 1.2v.4L8 9l6.5-4.4v-.4z"/></svg>admin@kelnovagroup.com.au</li>
        <li><svg viewBox="0 0 16 16"><circle cx="8" cy="8" r="7.5"/></svg>www.kelnovagroup.com.au</li>
      </ul>
    </div>
    <svg class="band" viewBox="0 0 800 90" preserveAspectRatio="none" aria-hidden="true">
      <polygon points="0,44 505,44 480,90 0,90" fill="var(--mid-blue)"/>
      <polygon points="525,20 800,20 800,90 492,90" fill="var(--navy)"/>
    </svg>
  </section>

  <section class="card card--back" aria-label="Business card back">
    <ul class="services">
      <li>Bookkeeping</li>
      <li>BAS</li>
      <li>Cloud Accounting</li>
      <li>Debt Recovery</li>
      <li>Business Advice</li>
      <li>ATO Assistance</li>
      <li>Office Technology</li>
      <li>&amp; Much More</li>
    </ul>
  </section>
</body>
</html>
```